Business Carss for Harborlight Church

Need a progressive looking/modern business card design for my church

Target Market(s)

Families and young adults

Industry/Entity Type

Religious

Contact Information for Business Card

4728 Willow Crest Rd.
Alderport Oh
614-318-4472

Rev. Tommy Fenwick
Slogan: Serve Others and Share Hope

Font styles to use
Serif
Sans Serif
Decorative
Script

Colors
0555a3
3176b5

Requirements
Should not have
• Should not have a template look
• A unique out of the box look

```html
<!DOCTYPE html>
<html lang="en">
<head>
<meta charset="utf-8">
<title>Harborlight Church – Business Card</title>
<link href="https://fonts.googleapis.com/css2?family=Marcellus&family=Montserrat:wght@400&family=Alex+Brush&family=Alegreya+Sans:wght@400&display=swap" rel="stylesheet">
<style>
  :root {
    --page: #c4c4c4;
    --card-dark: #0b0b0c;
    --card-dark-glow: #1c1c1f;
    --card-light: #f2f2f2;
    --card-light-edge: #e2e2e2;
    --ink-light: #f4f4f4;
    --rule-light: #a9a9a9;
    --brand-blue: #0555a3;
    --brand-blue-soft: #3176b5;
    --ink-dark: #3a3a3a;
  }
  html, body {
    margin: 0;
    width: 1200px;
    height: 1138px;
    overflow: hidden;
    background: var(--page);
  }
  .canvas { position: relative; width: 1200px; height: 1138px; }

  .card {
    position: absolute;
    width: 620px;
    height: 374px;
    border-radius: 16px;
    overflow: hidden;
  }

  /* Front */
  .card--front {
    left: 274px; top: 186px;
    background: var(--card-dark);
  }
  .front__bokeh {
    position: absolute; inset: 0;
    background:
      radial-gradient(ellipse 60% 45% at 45% 25%, var(--card-dark-glow), transparent 70%),
      radial-gradient(ellipse 40% 35% at 70% 65%, #151517, transparent 70%);
  }
  .front__name {
    position: absolute; left: 0; right: 0; top: 116px;
    text-align: center;
    font-family: "Marcellus", serif;
    font-weight: 400;
    font-size: 32px;
    letter-spacing: 1.5px;
    color: var(--ink-light);
    margin: 0;
    line-height: 1;
  }
  .front__divider { position: absolute; left: 125px; top: 164px; }
  .front__slogan {
    position: absolute; left: 0; right: 0; top: 196px;
    text-align: center;
    font-family: "Montserrat", sans-serif;
    font-size: 15px;
    letter-spacing: 3px;
    color: var(--ink-light);
    margin: 0;
  }
  .front__flourish {
    position: absolute; left: 256px; top: 242px;
    width: 110px; height: 14px;
    border-radius: 7px;
    background: linear-gradient(90deg, transparent, #9a9a9a 30%, #cfcfcf 50%, #9a9a9a 70%, transparent);
    opacity: .55;
  }

  /* Back */
  .card--back {
    left: 276px; top: 608px;
    background: linear-gradient(180deg, var(--card-light) 0%, #ffffff 40%, var(--card-light-edge) 100%);
  }
  .back__name {
    position: absolute; right: 40px; top: 50px;
    margin: 0;
    font-family: "Alex Brush", cursive;
    font-weight: 400;
    font-size: 34px;
    color: var(--brand-blue-soft);
    line-height: 1;
  }
  .back__slogan {
    position: absolute; right: 40px; top: 92px;
    margin: 0;
    font-family: "Alegreya Sans", sans-serif;
    font-size: 17px;
    color: var(--ink-dark);
  }
  .back__rule {
    position: absolute; left: 39px; right: 40px; top: 297px;
    height: 2px; background: var(--brand-blue);
  }
  .back__contact {
    position: absolute; left: 39px; top: 316px;
    display: flex; align-items: center; gap: 8px;
    font-family: "Alegreya Sans", sans-serif;
    font-size: 20px;
    color: var(--ink-dark);
  }
  .back__contact svg { fill: var(--brand-blue); }
  .back__contact .gap { width: 6px; }
</style>
</head>
<body>
<main class="canvas">
  <section class="card card--front">
    <div class="front__bokeh" role="img" aria-label="Soft dark bokeh light pattern"></div>
    <h1 class="front__name">REV. TOMMY FENWICK</h1>
    <svg class="front__divider" width="372" height="14" viewBox="0 0 372 14" aria-hidden="true">
      <line x1="0" y1="7" x2="172" y2="7" stroke="var(--rule-light)" stroke-width="1"/>
      <polygon points="186,0 188,5 193,5 189,8 191,13 186,10 181,13 183,8 179,5 184,5" fill="var(--ink-light)"/>
      <line x1="200" y1="7" x2="372" y2="7" stroke="var(--rule-light)" stroke-width="1"/>
    </svg>
    <p class="front__slogan">SERVE OTHERS AND SHARE HOPE</p>
    <div class="front__flourish" role="img" aria-label="Decorative silver flourish ornament"></div>
  </section>

  <section class="card card--back">
    <h2 class="back__name">Rev. Tommy Fenwick</h2>
    <p class="back__slogan">Serve Others and Share Hope</p>
    <div class="back__rule"></div>
    <div class="back__contact">
      <svg width="18" height="16" viewBox="0 0 18 16" aria-hidden="true">
        <path d="M1 5 C1 1 17 1 17 5 L17 7 L13 7 L13 5 L5 5 L5 7 L1 7 Z"/>
        <path d="M4 8 L14 8 L16 15 L2 15 Z"/>
      </svg>
      <span>614-318-4472</span>
      <span class="gap"></span>
      <svg width="14" height="20" viewBox="0 0 14 20" aria-hidden="true">
        <path d="M7 0 C3 0 0 3 0 7 C0 12 7 20 7 20 C7 20 14 12 14 7 C14 3 11 0 7 0 Z M7 4 A3 3 0 1 1 7 10 A3 3 0 1 1 7 4 Z"/>
      </svg>
      <span>4728 Willow Crest Rd.Alderport Oh</span>
    </div>
  </section>
</main>
</body>
</html>
```